Create a Mushroom Sticker design for a clothing Brand

We need a 2 sided Mushroom design for a die cut sticker that we want to put as a gift into our clothing orders. We want the front side of the sticker to be a simple black and white mushroom design surrounded by stars like the same stars that we have around our logo design the I included in the files. I also included some reference pictures of how I want the sticker to look like. I want small text under the mushroom design of our website url "Velto-Harbin.com". And on the back side of the mushroom sticker we want the text "Thank You !" (in big text)
"Dm us your Fits! @velto_harbin_ for a chance to be featured on our insta or LookBook page." (in smaller text)
We also want the sticker to be around 4 inches in height by 2.5 inches in width.
We want it to be a die cut sticker that surrounds the design Not a rectangular sticker.
Thank you designers can't wait to see what you can do!

```html
<!DOCTYPE html>
<html lang="en">
<head>
<meta charset="utf-8">
<title>Velto Harbin – Sticker Front and Back</title>
<link rel="stylesheet" href="https://fonts.googleapis.com/css2?family=Raleway:wght@400;500;700;800&family=Mrs+Saint+Delafield&display=swap">
<style>
  :root {
    --ink: #0b0b0b;
    --paper: #ffffff;
    --backdrop: #ececee;
    --text-dark: #2a2a2a;
    --frame-light: #d8d8d8;
    --art-top: #3a3a3a;
    --art-bottom: #141414;
  }
  * { margin: 0; padding: 0; box-sizing: border-box; }
  html, body { width: 1200px; height: 800px; overflow: hidden; }
  body {
    background: var(--backdrop);
    font-family: "Raleway", sans-serif;
    position: relative;
  }
  .sticker {
    position: absolute;
    top: 160px;
    width: 300px;
    height: 480px;
    box-shadow: 0 6px 18px rgba(0,0,0,0.18);
  }
  .sticker--front { left: 273px; background: var(--ink); color: var(--paper); }
  .sticker--back  { left: 620px; background: var(--paper); color: var(--text-dark); }
  .sticker__frame {
    position: absolute;
    inset: 8px;
    border: 1px solid var(--frame-light);
  }
  .sticker--back .sticker__frame { border-color: var(--ink); }

  .front__art {
    position: absolute;
    left: 22px; top: 55px;
    width: 256px; height: 250px;
    border-radius: 48% 48% 6px 6px;
    background: radial-gradient(ellipse at 50% 45%, var(--art-top), var(--art-bottom) 75%);
  }
  .front__url {
    position: absolute;
    left: 0; right: 0; top: 306px;
    text-align: center;
    font-size: 12px;
    letter-spacing: 2px;
    font-weight: 400;
  }
  .front__url strong { font-weight: 800; }
  .brand-name {
    position: absolute;
    left: 0; right: 0;
    text-align: center;
    font-weight: 800;
    text-transform: uppercase;
    line-height: 1.05;
  }
  .front__brand { top: 372px; font-size: 30px; letter-spacing: 2px; }

  .back__thanks {
    position: absolute;
    left: 0; right: 0; top: 30px;
    text-align: center;
    font-family: "Mrs Saint Delafield", cursive;
    font-size: 130px;
    line-height: 125px;
    color: var(--ink);
  }
  .back__message {
    position: absolute;
    left: 0; right: 0; top: 334px;
    text-align: center;
    font-size: 11px;
    line-height: 18px;
    letter-spacing: 0.8px;
    text-transform: uppercase;
  }
  .back__message strong { font-weight: 700; }
  .back__brand { top: 428px; font-size: 14px; letter-spacing: 1px; color: var(--ink); }
</style>
</head>
<body>
  <section class="sticker sticker--front">
    <div class="sticker__frame"></div>
    <div class="front__art" role="img" aria-label="White line illustration of three mushrooms with leaves, sprigs, a crescent moon and sparkling stars on a starry black sky"></div>
    <p class="front__url">www.<strong>Velto-Harbin</strong>.com</p>
    <p class="brand-name front__brand">Velto<br>Harbin</p>
  </section>

  <section class="sticker sticker--back">
    <div class="sticker__frame"></div>
    <h1 class="back__thanks">Thank<br>You!</h1>
    <p class="back__message">
      DM us your fits!<br>
      <strong>@velto_harbin_</strong> for a chance<br>
      to be featured on<br>
      our insta or look book page.
    </p>
    <p class="brand-name back__brand">Velto Harbin</p>
  </section>
</body>
</html>
```